Packaging & Label Design for CDB Products

We are a European CBD company specialising in athletic recovery, sleep improvement and wellness.

We would like the packaging to incorporate our logo and name (and font 'Codec') 'Meridell CBD'. The design must be transferable to all of our products. CBD Oils, Balms, Lip Balm and Vape E-Liquid.

We would like it to be simple but eye-catching and modern. We don't want bright colours. Preferred pallet of muted greys, blacks, white and pastel colours. Geometric concepts, possibly using different colours for each item of the range, we are open to new and fresh ideas (we are seeking you for your experience) and when we find the right design we would likely throw more work in your direction..

Our product range is not complete so the designer must be flexible with some changes and provide files where format can be easily edited by packaging manufacturer. We are also waiting for dimensions for the labels and boxes for several products and will supply the designer with full dimensions of all products once selected.

Oil Box: 2.6 x 9.0 x 2.6 cm (open format 16.7 x 11.6cm)
Labels: 7.8 x 3.3 cm (Front and Back)

Our expected product range will be:
CBD Oil 1000mg
CBD Oil 3000mg
CBD Balm 100mg
CBD Balm 300mg
E-Liquid 500mg
Lip Balm 50mg

We look forward to seeing your ideas.

Best Regards
Meridell CBD

```html
<!DOCTYPE html>
<html lang="en">
<head>
<meta charset="utf-8">
<title>Meridell CBD – Packaging Range</title>
<link href="https://fonts.googleapis.com/css2?family=Poppins:wght@300;400;600;700&display=swap" rel="stylesheet">
<style>
  :root {
    --navy: #2b2942;
    --white: #ffffff;
    --lilac: #d9c8dc;
    --sky: #c8dbf2;
    --sage: #bfc9b4;
    --sand: #e0cbb2;
    --sand-fold: #c9b296;
    --font: "Poppins", sans-serif;
  }
  html, body {
    margin: 0;
    padding: 0;
    width: 1200px;
    height: 1200px;
    overflow: hidden;
    background: var(--white);
    font-family: var(--font);
    color: var(--navy);
  }
  .canvas { position: relative; width: 1200px; height: 1200px; }

  .pack { position: absolute; overflow: hidden; }
  .pack__top {
    position: absolute; left: 0; top: 0; width: 100%;
    background: var(--navy);
    display: flex; flex-direction: column; align-items: center; justify-content: center;
  }
  .pack__bottom {
    position: absolute; left: 0; width: 100%; bottom: 0;
    display: flex; flex-direction: column; align-items: center;
    text-align: center;
  }

  .brand { display: flex; flex-direction: column; align-items: center; color: var(--white); }
  .brand__dot { border-radius: 50%; background: var(--white); }
  .brand__name { font-weight: 600; letter-spacing: 0.06em; white-space: nowrap; line-height: 1; }

  .tag { font-weight: 400; letter-spacing: 0.28em; white-space: nowrap; }
  .title { font-weight: 700; line-height: 1; white-space: nowrap; letter-spacing: -0.01em; }
  .sub { font-weight: 600; white-space: nowrap; }
  .note { font-weight: 400; letter-spacing: 0.3em; white-space: nowrap; }
  .dose { font-weight: 700; white-space: nowrap; }

  /* Lip balm */
  .lip { left: 180px; top: 372px; width: 54px; height: 184px; }
  .lip .pack__top { height: 102px; padding-top: 8px; box-sizing: border-box; }
  .lip .brand__dot { width: 14px; height: 14px; margin-bottom: 7px; }
  .lip .brand__name { font-size: 6.5px; letter-spacing: 0.02em; }
  .lip .pack__bottom { top: 102px; background: var(--lilac); padding-top: 13px; box-sizing: border-box; }
  .lip .tag { font-size: 3.5px; }
  .lip .title { font-size: 13px; margin-top: 3px; }
  .lip .sub { font-size: 6px; }
  .lip .note { font-size: 3px; margin-top: 4px; }
  .lip .dose { font-size: 4.5px; margin-top: 14px; }

  /* E-liquid */
  .liquid { left: 286px; top: 301px; width: 105px; height: 255px; }
  .liquid .pack__top { height: 142px; padding-top: 12px; box-sizing: border-box; }
  .liquid .brand__dot { width: 24px; height: 24px; margin-bottom: 12px; }
  .liquid .brand__name { font-size: 11px; }
  .liquid .pack__bottom { top: 142px; background: var(--sky); padding-top: 18px; box-sizing: border-box; }
  .liquid .tag { font-size: 5.5px; }
  .liquid .title { font-size: 20px; margin-top: 4px; }
  .liquid .sub { font-size: 9px; margin-top: 1px; }
  .liquid .note { font-size: 4.5px; margin-top: 6px; }
  .liquid .dose { font-size: 7px; margin-top: 21px; }

  /* Balm lid */
  .balm { left: 495px; top: 301px; width: 254px; height: 254px; border-radius: 50%; }
  .balm .pack__top { height: 142px; padding-top: 30px; box-sizing: border-box; }
  .balm .brand__dot { width: 38px; height: 38px; margin-bottom: 16px; }
  .balm .brand__name { font-size: 18px; }
  .balm .pack__bottom { top: 142px; background: var(--sage); padding-top: 16px; box-sizing: border-box; }
  .balm .tag { font-size: 9.5px; }
  .balm .title { font-size: 31px; margin-top: 5px; }
  .balm .note { font-size: 7.5px; margin-top: 3px; }
  .balm .dose { font-size: 10px; margin-top: 14px; }

  /* Oil bottle label */
  .label { left: 163px; top: 674px; width: 603px; height: 255px; }
  .label__band-top { position: absolute; left: 0; top: 0; width: 100%; height: 143px; background: var(--navy); }
  .label__band-bottom { position: absolute; left: 0; top: 143px; width: 100%; height: 112px; background: var(--sand); }
  .label__fold {
    position: absolute; top: 0; height: 100%; width: 16px;
    background: linear-gradient(to right, rgba(0,0,0,0), rgba(0,0,0,0.14));
  }
  .label__fold--left { left: 198px; }
  .label__fold--right { left: 390px; background: linear-gradient(to right, rgba(0,0,0,0.14), rgba(0,0,0,0)); }
  .label__front { position: absolute; left: 214px; top: 0; width: 176px; height: 100%; }
  .label .pack__top { height: 143px; padding-top: 8px; box-sizing: border-box; }
  .label .brand__dot { width: 38px; height: 38px; margin-bottom: 16px; }
  .label .brand__name { font-size: 16px; }
  .label .pack__bottom { top: 143px; padding-top: 24px; box-sizing: border-box; }
  .label .tag { font-size: 7.5px; }
  .label .title { font-size: 28px; margin-top: 3px; }
  .label .note { font-size: 6px; margin-top: 1px; }
  .label .dose { font-size: 8.5px; margin-top: 14px; }

  /* Oil box */
  .box { left: 830px; top: 235px; width: 201px; height: 696px; }
  .box .pack__top { height: 389px; justify-content: flex-start; padding-top: 98px; box-sizing: border-box; }
  .box .brand__dot { width: 58px; height: 58px; margin-bottom: 30px; }
  .box .brand__name { font-size: 22px; }
  .box .pack__bottom { top: 389px; background: var(--sand); padding-top: 28px; box-sizing: border-box; }
  .box .tag { font-size: 10px; }
  .box .title { font-size: 45px; margin-top: 52px; }
  .box .note { font-size: 8.5px; margin-top: 2px; }
  .box .dose { font-size: 11.5px; margin-top: 124px; }
</style>
</head>
<body>
<main class="canvas">

  <section class="pack lip" aria-label="Lip balm tube">
    <div class="pack__top">
      <div class="brand"><span class="brand__dot"></span><span class="brand__name">MERIDELL CBD</span></div>
    </div>
    <div class="pack__bottom">
      <span class="tag">-ALL NATURAL-</span>
      <span class="title">CBD</span>
      <span class="sub">Lip Balm</span>
      <span class="note">COLD PRESSED</span>
      <span class="dose">1000mg</span>
    </div>
  </section>

  <section class="pack liquid" aria-label="E-liquid box">
    <div class="pack__top">
      <div class="brand"><span class="brand__dot"></span><span class="brand__name">MERIDELL CBD</span></div>
    </div>
    <div class="pack__bottom">
      <span class="tag">-ALL NATURAL-</span>
      <span class="title">CBD</span>
      <span class="sub">E-Liquid</span>
      <span class="note">COLD PRESSED</span>
      <span class="dose">1000mg</span>
    </div>
  </section>

  <section class="pack balm" aria-label="Balm tin lid">
    <div class="pack__top">
      <div class="brand"><span class="brand__dot"></span><span class="brand__name">MERIDELL CBD</span></div>
    </div>
    <div class="pack__bottom">
      <span class="tag">-ALL NATURAL-</span>
      <span class="title">CBD Balm</span>
      <span class="note">COLD PRESSED</span>
      <span class="dose">100mg</span>
    </div>
  </section>

  <section class="pack label" aria-label="Oil bottle wrap label">
    <div class="label__band-top"></div>
    <div class="label__band-bottom"></div>
    <div class="label__fold label__fold--left"></div>
    <div class="label__fold label__fold--right"></div>
    <div class="label__front">
      <div class="pack__top">
        <div class="brand"><span class="brand__dot"></span><span class="brand__name">MERIDELL CBD</span></div>
      </div>
      <div class="pack__bottom">
        <span class="tag">-ALL NATURAL-</span>
        <span class="title">CBD Oil</span>
        <span class="note">COLD PRESSED</span>
        <span class="dose">1000mg</span>
      </div>
    </div>
  </section>

  <section class="pack box" aria-label="Oil carton front">
    <div class="pack__top">
      <div class="brand"><span class="brand__dot"></span><span class="brand__name">MERIDELL CBD</span></div>
    </div>
    <div class="pack__bottom">
      <span class="tag">-ALL NATURAL-</span>
      <span class="title">CBD Oil</span>
      <span class="note">COLD PRESSED</span>
      <span class="dose">1000mg</span>
    </div>
  </section>

</main>
</body>
</html>
```